Colourful Bold Design for Pet Insurance Website

PLEASE NOTE THAT THIS PROJECT HAS BEEN EXTENDED. Please read the PROJECT EXTENSION DOCUMENT BEFORE STARTING WORK ON ANY DESIGNS.

We are looking for a colourful bold new template design for our JOOMLA HOMEPAGE and a matching design for our new WORDPRESS BLOG.

The website will help pet owners work out which insurance policy best meets their needs. The aim of the website is to explain policy differences in a plain clear manner.

The website will need to have a professional colourful image. It needs to be BOLD, CLEAN AND SHARP rather than soft, pastel and cuddly.

COLOUR SCHEME
The website needs to have a bold colourful design on a white background.
On the inner pages we will have five different types of policies which will be colour coded. We would ideally therefore like to incorporate five distinct colours in the design. See attached document for example of colour schemes we like.

LOGO
We want to keep the existing logo. Please find the file attached. You may though change the logo colours.

CONTENT
One of the reasons for the new design is that we want to change the style of the homepage and include new content. Our current homepage can be found at www.furrow-cover-polls.co.uk.

Content Required
Slideshow
Article Intro.. About Pet Insurance
Policy Lookup Box (see existing site… you can change the design of this)
Six link options (see links on left of current page)
Latest Reviews (List of 6)
Ad (Same dimensions as currently on homepage)

News and Comment Section - To include Three or Four Articles, Title, Intro to article (probably 3 or 4 lines .. about 400px wide), Read more link
Social Media Section
Chatterly Plugin with Feed
Latest Tweets Plugin
Pet Charities Latest Tweets
Footer
Larger footer with lots of links grouped in sections

It does not need to include the clipart pic of the pets which is on the current homepage.

Examples of Websites and Templates We Like
http://www.pawlane.com/ (like colours… fonts…layout)
http://sitetheme.brightkiln.com/?template=upbeat&path=/... (like the clarity, "white" space etc)
http://www.layoutforge.com/demo/51872.html (like white space, clear easy to read fonts… don’t like colour scheme, size of top picture)
http://www.layoutforge.com/website-templates/63915.html (like colour scheme, use of white space)

FEEDBACK
I will provide lots of feedback on all designs submitted so that together we can get the best result.

For clarification this is a DESIGN ONLY project. Our website developer will view the designs before we make our final choice as he wants to ensure he can develop "sharp, practical and most importantly light weight web interface" from the design.

Just updated this brief to clarify design issues, content issues and to give some more examples of site designs I like. 

Please note that although we wish to keep the logo you can change the colours to suit your design. 

Please note that we have now added details of pictures we would be happy to use on the website.  We would prefer it if you used one of these.   Otherwise please ensure your picture includes a nice dog and nice cat and no people!

I have been delighted with the quality of the designs submitted for this project.  So much so that I am going to extend the project to include some additional inner pages.   The amended brief will be posted on here on Friday 10 May.   The deadline will be extended and the budget will also be increased. 

Reason: Additional inner pages now required. Budget will be increased. Revised brief to be posted on here Friday 10 May.

Target Market(s)

Pet owners in the UK who are confused about pet insurance. It therefore needs to be a bold design which is plain, clean and easy to read. It should use bold colours rather than pastels and should not use "cuddly" images.

Industry/Entity Type

Insurance

Requirements
Must have
• Bold clear and distinct colours (preferably 5)
Content as per uploaded file (not just content from existing site)
Easy to read fonts
Should not have
• Pastel colours
Cuddly images

```html
<!DOCTYPE html>
<html lang="en">
<head>
<meta charset="utf-8">
<title>Furrow Cover Polls UK</title>
<link href="https://fonts.googleapis.com/css2?family=Open+Sans:wght@400;600;700&family=Ubuntu:wght@400;500;700&display=swap" rel="stylesheet">
<style>
:root{
  --blue:#129fd3;
  --blue-dark:#0b86b9;
  --pink:#e3177f;
  --green:#2f9c2a;
  --green-bar:#1f9a1f;
  --red:#b9412f;
  --grey-text:#666;
  --line:#dedede;
  --page:#f3f4f5;
  --white:#fff;
}
*{box-sizing:border-box;margin:0;padding:0}
html,body{width:681px;height:1200px;overflow:hidden}
body{position:relative;background:var(--page);font-family:"Open Sans",Arial,sans-serif;color:var(--grey-text);font-size:7px;line-height:1.45}
.abs{position:absolute}
h1,h2,h3,h4{font-family:"Ubuntu",Arial,sans-serif;font-weight:400}

/* header */
.site-header{left:0;top:0;width:681px;height:104px;background:linear-gradient(#16a7da,#0d8fc2)}
.brand{left:60px;top:18px;display:flex;align-items:center;gap:7px;color:var(--white);font-family:"Ubuntu",sans-serif;font-weight:700;font-size:15px;line-height:1.05;width:150px}
.brand-mark{width:22px;height:22px;background:var(--white);flex:none}
.social{left:405px;top:7px;display:flex;gap:12px;align-items:center}
.social .dot{width:11px;height:11px;border-radius:50%;background:var(--white)}
.search{left:529px;top:5px;width:100px;height:20px;background:var(--white);border:1px solid #cfd8dd;font-size:8px;padding:4px 6px;color:#777}
.search-btn{left:609px;top:5px;width:20px;height:20px;background:#333}
.main-nav{left:253px;top:47px;width:376px;height:28px;background:var(--blue-dark);display:flex;justify-content:space-around;align-items:center;color:var(--white);font-size:8px}
.main-nav .current{position:relative}
.main-nav .current::after{content:"";position:absolute;left:50%;bottom:-9px;margin-left:-4px;border:4px solid transparent;border-bottom-color:var(--white)}

/* slider */
.slider{left:53px;top:77px;width:576px;height:227px;background:#f2f2f2;border:4px solid var(--white);box-shadow:0 0 3px rgba(0,0,0,.15)}
.slide-photo{left:26px;top:8px;width:240px;height:212px;background:radial-gradient(ellipse at 50% 55%,#bdb4a6,#e6e2dc 60%,#f2f2f2 75%)}
.slide-claim{left:286px;top:24px;width:280px;font-family:"Ubuntu",sans-serif;font-size:15px;line-height:1.45;color:#333}
.slide-claim .pink{color:var(--pink)}
.slide-claim .green{color:var(--green)}
.policy-box{left:339px;top:110px;width:175px;height:113px;background:#5ec7ee;padding:8px 10px}
.policy-box h2{color:var(--white);font-size:14px;margin-bottom:10px}
.select{height:18px;background:var(--white);margin-bottom:12px;position:relative;font-size:7px;padding:4px 8px;color:#555;width:150px}
.select::after{content:"";position:absolute;right:0;top:0;width:16px;height:18px;background:var(--blue)}
.select::before{content:"";position:absolute;right:4px;top:7px;border:4px solid transparent;border-top-color:var(--white);z-index:1}
.slider-dots{left:255px;top:203px;display:flex;gap:4px}
.slider-dots span{width:7px;height:7px;border-radius:50%;background:#555}
.slider-dots span:first-child{background:var(--blue)}
.arrow{top:173px;width:21px;height:22px;background:var(--blue)}

/* panels */
.panel{background:var(--white);border:1px solid var(--line)}
.panel-head{height:24px;color:var(--white);font-family:"Ubuntu",sans-serif;font-weight:500;font-size:10px;padding:5px 10px}
.welcome{left:57px;top:317px;width:384px;height:114px}
.welcome .panel-head{background:var(--blue)}
.welcome p{padding:0 13px;margin-top:9px;font-size:6.7px;line-height:1.5}
.reviews{left:57px;top:447px;width:227px;height:140px}
.reviews .panel-head{background:var(--red)}
.reviews ul{list-style:none;padding:7px 10px}
.reviews li{font-size:6.7px;padding-left:16px;position:relative;height:17px;line-height:10px;white-space:nowrap;overflow:hidden}
.reviews li::before{content:"";position:absolute;left:2px;top:2px;width:7px;height:7px;border-radius:50%;background:var(--blue)}
.offer{left:296px;top:447px;width:145px;height:140px;background:linear-gradient(135deg,#b98a5c,#7d5a3e 55%,#c7b9a6)}
.offer-tag{left:296px;top:455px;background:var(--blue);color:var(--white);font-weight:700;font-size:10px;padding:2px 7px;font-family:"Ubuntu",sans-serif}
.offer-cta{left:300px;top:567px;width:137px;height:17px;background:var(--pink);color:var(--white);font-size:7px;padding:2px 6px;white-space:nowrap}
.offer-cta b{font-size:10.5px}
.news{left:57px;top:603px;width:384px;height:338px}
.news .panel-head{background:var(--green-bar)}
.article{left:12px;width:358px}
.article h3{color:var(--blue);font-size:9.5px;margin-bottom:5px}
.article p{font-size:6.8px;line-height:1.55}
.article .more{display:block;margin-top:4px;color:#333;font-weight:600;font-size:6.8px}
.article .more span{color:var(--blue)}
.divider{left:12px;width:358px;height:1px;background:var(--line)}

/* sidebar */
.side{left:457px;width:164px;padding:8px 9px}
.side h4{font-size:11px;color:#555;margin-bottom:4px}
.side h4 em{font-style:normal;color:var(--blue)}
.side p{font-size:6.3px;line-height:1.45}
.fb{left:461px;top:795px;width:158px;height:198px;background:var(--white);border:1px solid #c4c4c4;font-size:6px;color:#333}
.fb-head{background:#eceff5;font-weight:700;font-size:6.5px;padding:3px 5px;border-bottom:1px solid #ccc}
.fb-row{display:flex;gap:4px;padding:3px 5px}
.avatar{width:13px;height:13px;background:#9aa3ad;flex:none}
.avatar.sm{width:18px;height:16px}
.fb-name{color:#3b5998;font-weight:700}
.fb-grid{display:flex;flex-wrap:wrap;gap:2px;padding:2px 5px}

/* footer */
.site-footer{left:0;top:1020px;width:681px;height:180px;background:linear-gradient(#149fd4,#0a86bb)}
.foot-col{top:1067px;color:var(--white)}
.foot-col h4{font-size:11px;font-weight:700;margin-bottom:9px}
.foot-col ul{list-style:none}
.foot-col li{font-size:7px;height:13.7px;padding-left:10px;position:relative;white-space:nowrap}
.foot-col li::before{content:"›";position:absolute;left:0;top:-1px;font-weight:700}
.foot-brand{left:482px;top:1094px}
.copyright{left:484px;top:1145px;color:var(--white);font-size:6.5px}
</style>
</head>
<body>

<header class="site-header abs">
  <div class="brand abs"><span class="brand-mark"></span><span>Furrow Cover Polls UK</span></div>
  <div class="social abs">
    <svg width="11" height="11" viewBox="0 0 12 12"><circle cx="9" cy="2.5" r="2" fill="#fff"/><circle cx="3" cy="6" r="2" fill="#fff"/><circle cx="9" cy="9.5" r="2" fill="#fff"/><path d="M9 2.5 3 6l6 3.5" stroke="#fff" fill="none"/></svg>
    <span class="dot"></span>
    <span class="dot"></span>
    <svg width="11" height="11" viewBox="0 0 12 12"><circle cx="2" cy="10" r="1.6" fill="#fff"/><path d="M1 5.5a5.5 5.5 0 0 1 5.5 5.5M1 1.5A9.5 9.5 0 0 1 10.5 11" stroke="#fff" stroke-width="1.8" fill="none"/></svg>
    <svg width="12" height="10" viewBox="0 0 12 10"><rect x=".5" y=".5" width="11" height="9" fill="none" stroke="#fff"/><path d="M.5.5 6 5.5 11.5.5" stroke="#fff" fill="none"/></svg>
  </div>
  <div class="search abs">Search</div>
  <div class="search-btn abs"><svg width="20" height="20" viewBox="0 0 20 20"><circle cx="9" cy="9" r="4" stroke="#fff" stroke-width="1.5" fill="none"/><path d="m12 12 4 4" stroke="#fff" stroke-width="1.8"/></svg></div>
  <nav class="main-nav abs">
    <span class="current">Home</span><span>Policies</span><span>Glossary</span><span>Fact Sheets</span><span>Survey Reports</span><span>News &amp; Comment</span>
  </nav>
</header>

<section class="slider abs">
  <div class="slide-photo abs" role="img" aria-label="Photo of a large spotted dog, a parrot, a cat, a puppy and a rabbit sitting together"></div>
  <p class="slide-claim abs">We do not <span class="pink">sell pet insurance...</span> or <span class="green">receive commission</span> from <span class="pink">pet insurance companies...</span></p>
  <div class="policy-box abs">
    <h2>Policies Out here</h2>
    <div class="select">Select Company</div>
    <div class="select">Select Policy</div>
  </div>
  <div class="slider-dots abs"><span></span><span></span><span></span><span></span></div>
</section>
<div class="arrow abs" style="left:45px"><svg width="21" height="22" viewBox="0 0 21 22"><path d="M13 6 8 11l5 5" stroke="#fff" stroke-width="2" fill="none"/></svg></div>
<div class="arrow abs" style="left:616px"><svg width="21" height="22" viewBox="0 0 21 22"><path d="m8 6 5 5-5 5" stroke="#fff" stroke-width="2" fill="none"/></svg></div>

<section class="welcome panel abs">
  <h2 class="panel-head">Welcome to Furrow Cover Polls UK</h2>
  <p>This is an independent website dedicated to helping you to find the best pet insurance policy for your pet</p>
  <p>Here you will find unbiased detailed information about almost all of the 205 pet insurance policies<br>currently available in the UK (we hope the other 3 will follow shortly!)</p>
  <p>We do NOT sell any pet insurance policies nor do we receive commission from any insurance companies</p>
</section>

<section class="reviews panel abs">
  <h2 class="panel-head">Latest Reviews</h2>
  <ul>
    <li>Lorem ipsum dolor sit amet, consectetur uscipit nec</li>
    <li>Donec tellus nibh, suscipit nec ultrices ac suscipit nec</li>
    <li>Nullam ac odio justo, sed cursus augue. ed cursus au.</li>
    <li>Praesent consequat condimentum ullamcorper consewt.</li>
    <li>Aliquam vitae mi quis purus bibendum eleme quis purus</li>
    <li>Aenean fermentum ante nec libero laoreet laoreet</li>
  </ul>
</section>

<div class="offer abs" role="img" aria-label="Photo of a cat and a basset hound side by side"></div>
<div class="offer-tag abs">OFFER</div>
<div class="offer-cta abs">click here for <b>20% discount</b></div>

<section class="news panel abs">
  <h2 class="panel-head">Latest News &amp; Comments</h2>
  <article class="article abs" style="top:36px">
    <h3>Donec tellus nibh</h3>
    <p>Nunc metus nisi, cursus sed commodo sed, vestibulum ac enim. Vestibulum malesuada dolor in urna fringilla sit amet placerat magna rhoncus. it amet placerat magna rhoncus. Nunc metus nisi, cursus sed commodo sed, vestibulum ac enim. Vestibulum malesuada dolor in urna fringilla sit amet placerat magna rhoncus. it amet placerat magna rhoncus.</p>
    <a class="more">Read More <span>»</span></a>
  </article>
  <div class="divider abs" style="top:134px"></div>
  <article class="article abs" style="top:143px">
    <h3>Donec tellus nibh</h3>
    <p>Nunc metus nisi, cursus sed commodo sed, vestibulum ac enim. Vestibulum malesuada dolor in urna fringilla sit amet placerat magna rhoncus. it amet placerat magna rhoncus. Nunc metus nisi, cursus sed commodo sed, vestibulum ac enim. Vestibulum malesuada dolor in urna fringilla sit amet placerat magna rhoncus. it amet placerat magna rhoncus.</p>
    <a class="more">Read More <span>»</span></a>
  </article>
  <div class="divider abs" style="top:241px"></div>
  <article class="article abs" style="top:250px">
    <h3>Donec tellus nibh</h3>
    <p>Nunc metus nisi, cursus sed commodo sed, vestibulum ac enim. Vestibulum malesuada dolor in urna fringilla sit amet placerat magna rhoncus. it amet placerat magna rhoncus. Nunc metus nisi, cursus sed commodo sed, vestibulum ac enim. Vestibulum malesuada dolor in urna fringilla sit amet placerat magna rhoncus. it amet placerat magna rhoncus.</p>
    <a class="more">Read More <span>»</span></a>
  </article>
</section>

<aside>
  <div class="side panel abs" style="top:317px;height:108px"><h4><em>Policy</em> Files</h4><p>Full policy details including type of vet fees cover and limits, ratings, age limits, excess details, benefits and terms analysisFull policy details including type of vet fees cover and limits, ratings, age limits, excess details, benefits and terms analysis</p></div>
  <div class="side panel abs" style="top:432px;height:64px"><h4><em>Fact</em> Sheets</h4><p>Learn about pet insurance. A little knowledge is essential to choosing the right policy</p></div>
  <div class="side panel abs" style="top:501px;height:74px"><h4><em>Policy Listings</em> by Type</h4><p>Full lists of continuous policies (aka "lifetime policies), 12- month policies and accident policies.</p></div>
  <div class="side panel abs" style="top:583px;height:73px"><h4><em>Claims</em> Survey</h4><p>Made a claim in the last 12 months? Please help us to help others by completing this 2-minute survey</p></div>
  <div class="side panel abs" style="top:665px;height:60px"><h4><em>Policy</em> Search</h4><p>Exclusive to FCP friends. Search our database of more than 200 policies</p></div>
  <div class="side panel abs" style="top:733px;height:46px"><h4><em>2013 Price Survey</em> Report</h4><p>Due April 2013</p></div>

  <div class="fb abs">
    <div class="fb-head">Find us on Chatterly</div>
    <div class="fb-row"><span class="avatar"></span><div><span class="fb-name">Dale Orwin</span><br>Like · You like this.</div></div>
    <div class="fb-row"><span class="avatar"></span><div><span class="fb-name">Dale Orwin</span><br>Think all of the town should throw a party for my birthday this year.<br><span style="color:#999">Thursday at 2:10pm</span></div></div>
    <div class="fb-row"><span class="avatar"></span><div><span class="fb-name">Dale Orwin</span><br>Tell your friends to give you five in advertising credit for FREE. Such a deal!</div></div>
    <div class="fb-row" style="padding-top:0">You and 25,596 others like <span class="fb-name">Dale Orwin</span>.</div>
    <div class="fb-grid">
      <span class="avatar sm"></span><span class="avatar sm"></span><span class="avatar sm"></span><span class="avatar sm"></span><span class="avatar sm"></span><span class="avatar sm"></span>
      <span class="avatar sm"></span><span class="avatar sm"></span><span class="avatar sm"></span><span class="avatar sm"></span><span class="avatar sm"></span><span class="avatar sm"></span>
    </div>
    <div style="padding:2px 5px;color:#777">Social plugin</div>
  </div>
</aside>

<footer class="site-footer abs"></footer>
<div class="foot-col abs" style="left:69px"><h4>Nunc metus nisi</h4><ul><li>Nunc metus nisi,</li><li>Cursus sed commodo sed,</li><li>Vestibulum malesua</li><li>Placerat magna rhoncus.</li><li>Nunc metus nisi,</li><li>Cursus sed commodo sed,</li><li>Vestibulum malesua</li></ul></div>
<div class="foot-col abs" style="left:205px"><h4>Nunc metus nisi</h4><ul><li>Nunc metus nisi,</li><li>Cursus sed commodo sed,</li><li>Vestibulum malesua</li><li>Placerat magna rhoncus.</li><li>Nunc metus nisi,</li><li>Cursus sed commodo sed,</li><li>Vestibulum malesua</li></ul></div>
<div class="foot-col abs" style="left:341px"><h4>Nunc metus nisi</h4><ul><li>Nunc metus nisi,</li><li>Cursus sed commodo sed,</li><li>Vestibulum malesua</li><li>Placerat magna rhoncus.</li><li>Nunc metus nisi,</li><li>Cursus sed commodo sed,</li><li>Vestibulum malesua</li></ul></div>
<div class="brand foot-brand abs"><span class="brand-mark"></span><span>Furrow Cover Polls UK</span></div>
<p class="copyright abs">copyright © Furrow Cover Polls</p>

</body>
</html>
```